Austin Motivated Sellers #1

I am A local real estate investor in the highly competitive single family homes market of Austin,Tx.for fix and flipping My company uses several nontraditional and creative solutions for helping home owners sell their faster for cash with a closing date of their choice and helps them save thousands of dollars in having to pay real estate commissions and fees.My idea for the front of the postcard is to show the home owner what they could do with all the money they'll save by selling their home with us.I want a background picture on the front of taking a vacation with the money they'll save, or down payment on a new car on the back or even just a pile of cash they'll save to do whatever they like with.
Company name: Bold Harbor Properties
website: www.Quickdeedoffer.example
phone # : 512-555-0187 / 24hr.recorded message

Industry/Entity Type

Real Estate

```html
<!DOCTYPE html>
<html lang="en">
<head>
<meta charset="utf-8">
<title>Bold Harbor Properties – Postcard</title>
<link rel="stylesheet" href="https://fonts.googleapis.com/css2?family=Roboto:wght@400;700;900&family=Oswald:wght@400;500&family=Roboto+Condensed:wght@300;400;700&family=Questrial&family=Open+Sans:wght@400;600;700;800&display=swap">
<style>
  :root {
    --red: #c8102e;
    --blue: #1a5aa6;
    --blue-deep: #13488c;
    --ink: #1b1b1b;
    --text: #333333;
    --paper: #ffffff;
    --backdrop: #e9e9e9;
    --rule: #8a8a8a;
  }
  * { box-sizing: border-box; margin: 0; padding: 0; }
  html, body { width: 890px; height: 1200px; overflow: hidden; background: var(--backdrop); }
  .sheet { position: relative; width: 890px; height: 1200px; }
  .card-slot { position: absolute; left: 45px; width: 800px; height: 535px; }
  .card-slot.front-slot { top: 45px; }
  .card-slot.back-slot { top: 620px; }
  .card {
    position: absolute; left: 0; top: 0; width: 893px; height: 597px;
    transform: scale(0.896); transform-origin: 0 0;
    background: var(--paper); overflow: hidden;
    box-shadow: 0 4px 14px rgba(0,0,0,.25);
    font-family: "Open Sans", sans-serif;
  }
  .abs { position: absolute; }

  /* Front */
  .brand { left: 38px; top: 62px; display: flex; align-items: center; gap: 8px; }
  .brand-dot { width: 14px; height: 14px; background: var(--red); }
  .brand-name { font-family: "Open Sans", sans-serif; font-weight: 600; font-size: 19px; line-height: 1.15; color: var(--blue-deep); width: 120px; }
  .hero-photo { left: 10px; top: 30px; width: 505px; height: 430px;
    background: radial-gradient(ellipse at 52% 45%, #dcdde0 0%, #eef0f2 45%, #ffffff 75%); }
  .call-band { left: 0; top: 440px; width: 893px; height: 157px; }
  .call-label { left: 65px; top: 470px; width: 380px; display: flex; align-items: center; gap: 10px;
    font-family: "Oswald", sans-serif; font-size: 24px; color: #fff; }
  .call-label::before, .call-label::after { content: ""; flex: 1; height: 2px; background: var(--red); }
  .phone-row { left: 58px; top: 500px; display: flex; align-items: center; gap: 12px; }
  .phone-number { font-family: "Oswald", sans-serif; font-weight: 500; font-size: 50px; color: #fff; letter-spacing: 2px; }
  .web-line { left: 113px; top: 561px; font-size: 13px; color: #fff; }
  .web-line .url { color: var(--red); font-weight: 700; margin-left: 4px; }
  .headline-sell { left: 522px; top: 20px; font-family: "Roboto", sans-serif; font-weight: 900; font-size: 132px; line-height: 1; color: var(--red); letter-spacing: 3px; }
  .headline-home { left: 522px; top: 146px; font-family: "Roboto", sans-serif; font-weight: 900; font-size: 32px; color: var(--blue-deep); }
  .rule-red { left: 522px; width: 340px; height: 1px; background: var(--red); }
  .headline-save { left: 522px; top: 192px; font-family: "Roboto", sans-serif; font-weight: 900; font-size: 37px; color: var(--red); }
  .headline-fees { left: 522px; top: 232px; font-family: "Roboto", sans-serif; font-weight: 700; font-size: 24px; color: var(--blue-deep); }
  .intro { left: 522px; top: 276px; width: 345px; font-family: "Questrial", sans-serif; font-size: 17px; line-height: 21px; color: var(--ink); }
  .offer-box { left: 515px; top: 387px; width: 378px; height: 166px; border: 2px solid var(--red); border-right: none; background: #fff; }
  .offer-badge { left: 518px; top: 350px; width: 72px; height: 72px; border-radius: 50%; background: var(--blue);
    box-shadow: 0 0 0 3px #fff, 0 0 0 5px var(--blue);
    color: #fff; font-family: "Oswald", sans-serif; font-size: 25px; display: flex; align-items: center; justify-content: center; }
  .offer-tag { left: 594px; top: 364px; width: 158px; height: 50px; background: var(--red);
    clip-path: polygon(0 0, 100% 0, 93% 100%, 0 100%);
    color: #fff; font-family: "Open Sans", sans-serif; font-weight: 800; font-size: 16px; line-height: 16px; padding: 9px 0 0 10px; }
  .benefits { left: 562px; top: 425px; list-style: none; font-family: "Questrial", sans-serif; font-size: 14.5px; color: var(--ink); }
  .benefits li { display: flex; align-items: center; gap: 9px; height: 24.5px; }
  .benefits svg { width: 11px; height: 11px; flex: none; }
  .help-line { right: 14px; top: 564px; font-family: "Questrial", sans-serif; font-size: 19px; color: #fff; }

  /* Back */
  .desk-photo { left: 0; top: 0; width: 468px; height: 258px;
    background: linear-gradient(180deg, #4d5663 0%, #9aa2ac 45%, #c9ccd0 75%, #b3b7bc 100%); }
  .back-divider { left: 440px; top: 0; width: 40px; height: 597px; }
  .banner { left: 0; top: 255px; width: 392px; height: 36px; background: var(--red);
    clip-path: polygon(0 0, 100% 0, 94% 100%, 0 100%);
    color: #fff; font-family: "Open Sans", sans-serif; font-weight: 700; font-size: 15.5px; padding: 7px 0 0 22px; }
  .story { left: 37px; top: 303px; width: 390px; font-family: "Roboto Condensed", sans-serif; font-weight: 300; font-size: 13px; line-height: 19.5px; color: var(--ink); letter-spacing: -.2px; }
  .story p { margin-bottom: 4px; }
  .story strong { color: var(--red); font-weight: 700; }
  .cta-bar { left: 0; top: 480px; width: 462px; height: 37px; background: #111;
    color: #fff; font-family: "Open Sans", sans-serif; font-size: 15.5px; padding: 8px 0 0 18px; }
  .cta-bar b { font-weight: 800; }
  .cta-contact { left: 0; top: 517px; width: 462px; height: 80px; background: var(--blue);
    color: #fff; font-family: "Open Sans", sans-serif; font-size: 15.5px; line-height: 24px; padding: 12px 0 0 20px; }
  .cta-contact b { font-weight: 700; }
  .stamp-box { left: 773px; top: 38px; width: 90px; height: 90px; border: 1px solid var(--rule); }
  .address-line { left: 563px; width: 300px; height: 1px; background: var(--rule); }
  .back-brand { left: 600px; top: 490px; width: 180px; display: flex; align-items: center; justify-content: center; gap: 7px; }
  .back-brand .brand-dot { width: 11px; height: 11px; }
  .back-brand .brand-name { font-size: 14px; width: auto; text-align: center; }
  .back-help { left: 560px; top: 560px; width: 260px; text-align: center; font-family: "Open Sans", sans-serif; font-size: 14px; color: var(--red); }
</style>
</head>
<body>
<main class="sheet">

  <div class="card-slot front-slot">
    <section class="card front">
      <div class="abs hero-photo" role="img" aria-label="Smiling man in shirt and tie holding up stacks of cash in both hands"></div>

      <div class="abs brand">
        <span class="brand-dot"></span>
        <span class="brand-name">Bold Harbor Properties</span>
      </div>

      <svg class="abs call-band" viewBox="0 0 893 157" preserveAspectRatio="none">
        <path d="M0 10 Q260 -6 515 10 L515 157 L0 157 Z" fill="#c8102e"/>
        <path d="M0 22 Q260 4 515 20 L515 157 L0 157 Z" fill="#1a5aa6"/>
        <rect x="515" y="112" width="378" height="45" fill="#1a5aa6"/>
      </svg>

      <div class="abs call-label">CALL US AT:</div>
      <div class="abs phone-row">
        <svg width="32" height="32" viewBox="0 0 24 24" aria-hidden="true">
          <path d="M6.6 10.8a15.5 15.5 0 0 0 6.6 6.6l2.2-2.2c.3-.3.7-.4 1-.2 1.1.4 2.3.6 3.6.6.6 0 1 .4 1 1V20c0 .6-.4 1-1 1A17 17 0 0 1 3 4c0-.6.4-1 1-1h3.5c.6 0 1 .4 1 1 0 1.3.2 2.5.6 3.6.1.3 0 .7-.2 1l-2.3 2.2z" fill="#fff"/>
        </svg>
        <span class="phone-number">512-555-0187</span>
        <svg width="66" height="48" viewBox="0 0 66 48" aria-hidden="true">
          <circle cx="30" cy="24" r="20" fill="none" stroke="#c8102e" stroke-width="3"/>
          <text x="30" y="24" text-anchor="middle" font-family="Oswald, sans-serif" font-size="18" font-weight="500" fill="#fff">24/7</text>
          <rect x="2" y="28" width="62" height="10" fill="#c8102e" transform="rotate(-8 33 33)"/>
          <text x="33" y="36" text-anchor="middle" font-family="Open Sans, sans-serif" font-size="6" font-weight="700" fill="#fff" transform="rotate(-8 33 33)">RECORDED MESSAGE</text>
        </svg>
      </div>
      <div class="abs web-line">or visit out website:<span class="url">www.Quickdeedoffer.example</span></div>

      <div class="abs headline-sell">SELL</div>
      <div class="abs headline-home">YOUR HOME WITH US!</div>
      <div class="abs rule-red" style="top:189px"></div>
      <div class="abs headline-save">SAVE THOUSANDS</div>
      <div class="abs headline-fees">in Commissions and Fees</div>
      <div class="abs rule-red" style="top:266px"></div>
      <p class="abs intro">Did you know there are at least a 12 Different Ways to Sell Your Property that Realtors won't tell you about?</p>

      <div class="abs offer-box"></div>
      <div class="abs offer-badge">100%</div>
      <div class="abs offer-tag">GUARANTEED<br>CASH OFFER</div>
      <ul class="abs benefits">
        <li><svg viewBox="0 0 12 12"><rect x="1" y="2" width="9" height="9" fill="none" stroke="#c8102e" stroke-width="1.3"/><path d="M3 6l2.5 2.5L11 1.5" fill="none" stroke="#c8102e" stroke-width="1.6"/></svg>We Buy Properties Fast</li>
        <li><svg viewBox="0 0 12 12"><rect x="1" y="2" width="9" height="9" fill="none" stroke="#c8102e" stroke-width="1.3"/><path d="M3 6l2.5 2.5L11 1.5" fill="none" stroke="#c8102e" stroke-width="1.6"/></svg>We buy with cash</li>
        <li><svg viewBox="0 0 12 12"><rect x="1" y="2" width="9" height="9" fill="none" stroke="#c8102e" stroke-width="1.3"/><path d="M3 6l2.5 2.5L11 1.5" fill="none" stroke="#c8102e" stroke-width="1.6"/></svg>We have many creative solutions available</li>
        <li><svg viewBox="0 0 12 12"><rect x="1" y="2" width="9" height="9" fill="none" stroke="#c8102e" stroke-width="1.3"/><path d="M3 6l2.5 2.5L11 1.5" fill="none" stroke="#c8102e" stroke-width="1.6"/></svg>Choose your closing Date</li>
        <li><svg viewBox="0 0 12 12"><rect x="1" y="2" width="9" height="9" fill="none" stroke="#c8102e" stroke-width="1.3"/><path d="M3 6l2.5 2.5L11 1.5" fill="none" stroke="#c8102e" stroke-width="1.6"/></svg>We buy as is .. No repairs necessary</li>
      </ul>
      <div class="abs help-line">Let Us Know How We Can Help!</div>
    </section>
  </div>

  <div class="card-slot back-slot">
    <section class="card back">
      <div class="abs desk-photo" role="img" aria-label="Hands of a man in a suit counting cash into three piles labelled Vacation, Car Payment and College"></div>
      <svg class="abs back-divider" viewBox="0 0 40 597" preserveAspectRatio="none" aria-hidden="true">
        <path d="M8 0 L28 0 Q30 120 30 597 L10 597 Q10 200 8 0 Z" fill="#1a5aa6"/>
        <path d="M28 0 L33 0 Q35 120 35 597 L30 597 Q30 120 28 0 Z" fill="#c8102e"/>
      </svg>
      <div class="abs banner">Save thousands selling your house with us!</div>
      <div class="abs story">
        <p>We are a local cash buyer here in Austin and we use some creative and nontraditional solutions most realtors don't know about or won't tell you that can literally save you thousands in expensive commissions and fees.</p>
        <p>If you are like most sellers, you want to explore how to sell your property fast and hassle free. We can help! That's what we do...</p>
        <p><strong>We Buy Properties Fast...</strong> regardless of condition, equity, or situation. We've handled just about every situation you can imagine. We buy with cash. We even have many creative solutions available. We are experts.</p>
      </div>
      <div class="abs cta-bar"><b>CALL US NOW!</b> &nbsp;- &nbsp;100% GUARANTEED CASH OFFER</div>
      <div class="abs cta-contact">call <b>512-555-0187</b> / 24hr.recorded message<br>or visit our website: <b>www.Quickdeedoffer.example</b></div>

      <div class="abs stamp-box"></div>
      <div class="abs address-line" style="top:233px"></div>
      <div class="abs address-line" style="top:270px"></div>
      <div class="abs address-line" style="top:305px"></div>
      <div class="abs address-line" style="top:342px"></div>

      <div class="abs back-brand">
        <span class="brand-dot"></span>
        <span class="brand-name">Bold Harbor Properties</span>
      </div>
      <div class="abs back-help">Let Us Know How We Can Help!</div>
    </section>
  </div>

</main>
</body>
</html>
```